Real Estate Team Needs Business Cards

Double sided - Team Member on Front, Team Leader on Back (back side will contain more details).
Colors to use:
Red = R: 233 G: 1 B: 2
Grey = R: 89 G: 89 B: 89
Black= R: 0 B: 0 B: 0
** MAIN FOCUS ** ( separate border, color, design, etc. to really stand out - whatever you think draws the most attention ) on both sides for "Sell for 1%‡" and "Buy & receive up to a 1% rebate‡". Must have fine print **
**Please make both sides stand out and look unique / different
Business card to have round corners (standard size 3.5" x 2").:
Document Trim Size
89 x 51 mm
1050 x 600 pixels
Full Bleed Size
92 x 54 mm
1085 x 635 pixels
Basic example provided. Please redesign as you see best. In your design - Please use the same picture on both sides. Name, address, phone number, email, etc. will be provided to the selected design. QR code on back side only if there is room (not important)

```html
<!DOCTYPE html>
<html lang="en">
<head>
<meta charset="utf-8">
<title>Brightline Realty – Business Card</title>
<link href="https://fonts.googleapis.com/css2?family=Lato:wght@400;700&display=swap" rel="stylesheet">
<style>
  :root {
    --brand-red: #e81f26;
    --text-grey: #8a8a8a;
    --page-bg: #e0e0e0;
    --card-white: #ffffff;
    --suit-navy: #1f3f7a;
    --shirt-light: #eef2f6;
  }
  * { margin: 0; padding: 0; box-sizing: border-box; }
  html, body { width: 1200px; height: 960px; overflow: hidden; }
  body {
    background: var(--page-bg);
    font-family: "Lato", Arial, sans-serif;
    position: relative;
  }
  .card {
    position: absolute;
    left: 281px;
    width: 655px;
    height: 374px;
    border-radius: 20px;
    overflow: hidden;
  }
  .card--front { top: 80px; background: var(--card-white); }
  .card--back { top: 506px; background: var(--brand-red); color: #fff; text-align: center; }

  .portrait {
    position: absolute;
    left: 0; bottom: 0;
    width: 280px; height: 340px;
    background: linear-gradient(180deg, var(--shirt-light) 0%, #c9d3e2 35%, var(--suit-navy) 70%, #17305f 100%);
    border-top-right-radius: 120px;
  }

  .details { position: absolute; left: 318px; top: 62px; }
  .person-name { color: var(--brand-red); font-weight: 700; font-size: 29px; line-height: 1; letter-spacing: 0.2px; }
  .person-role { color: var(--text-grey); font-size: 18.5px; margin-top: 6px; }
  .offer-headline { color: var(--brand-red); font-weight: 700; font-size: 26px; margin-top: 20px; line-height: 1; }
  .offer-sub { color: var(--text-grey); font-size: 17px; margin-top: 8px; }
  .contact-list { list-style: none; margin-top: 14px; }
  .contact-list li { color: var(--text-grey); font-size: 17.5px; height: 23.5px; display: flex; align-items: center; gap: 8px; }
  .contact-list svg { width: 13px; height: 13px; flex: none; }

  .brand-name { position: absolute; left: 0; right: 0; top: 165px; font-weight: 700; font-size: 28px; letter-spacing: 1px; display: flex; justify-content: center; align-items: center; gap: 10px; }
  .brand-mark { width: 16px; height: 16px; background: #fff; }
  .back-headline { position: absolute; left: 0; right: 0; top: 216px; font-weight: 700; font-size: 26px; line-height: 1; }
  .back-sub { position: absolute; left: 0; right: 0; top: 243px; font-size: 17.5px; }
  .web-rule { position: absolute; left: 0; right: 0; top: 309px; display: flex; align-items: center; gap: 8px; font-size: 17.5px; }
  .web-rule::before, .web-rule::after { content: ""; flex: 1; height: 1px; background: rgba(255,255,255,0.75); }
</style>
</head>
<body>
  <section class="card card--front">
    <div class="portrait" role="img" aria-label="Portrait photo of the team leader in a navy suit and light blue tie"></div>
    <div class="details">
      <h1 class="person-name">DANIEL MARSH</h1>
      <p class="person-role">Founder &amp; CEO</p>
      <p class="offer-headline">Sell for 1%*</p>
      <p class="offer-sub">Buy &amp; receive up to a 1% rebate*</p>
      <ul class="contact-list">
        <li><svg viewBox="0 0 12 12"><rect x="3" y="0.8" width="6" height="10.4" rx="1" fill="none" stroke="var(--brand-red)" stroke-width="1.4"/></svg>(555) 010 2030</li>
        <li><svg viewBox="0 0 12 12"><path d="M2 11 C2 6 5 2 11 1.5 L11 4 L8.5 4.5 C6 5.5 4.5 7.5 4.3 10.5 Z" fill="var(--brand-red)"/></svg>(555) 010 4050</li>
        <li><svg viewBox="0 0 12 12"><rect x="0.5" y="2.5" width="11" height="7" fill="var(--brand-red)"/><path d="M0.5 2.5 L6 6.5 L11.5 2.5 M0.5 9.5 L4.5 6 M11.5 9.5 L7.5 6" fill="none" stroke="#fff" stroke-width="1"/></svg>info@brightlinerealty.com</li>
        <li><svg viewBox="0 0 12 12"><g fill="none" stroke="var(--brand-red)" stroke-width="1.1"><circle cx="6" cy="6" r="5.2"/><ellipse cx="6" cy="6" rx="2.2" ry="5.2"/><path d="M0.8 6 H11.2 M1.8 3.3 H10.2 M1.8 8.7 H10.2"/></g></svg>www.brightlinerealty.com</li>
      </ul>
    </div>
  </section>

  <section class="card card--back">
    <div class="brand-name"><span class="brand-mark"></span>BRIGHTLINE REALTY</div>
    <p class="back-headline">Sell for 1%*</p>
    <p class="back-sub">Buy &amp; receive up to a 1% rebate*</p>
    <p class="web-rule">www.brightlinerealty.com</p>
  </section>
</body>
</html>
```